Update our OBGYN business card look and info

We are an OBGYN office. Our logo is nice but would like to "woman" part of the logo to be a darker color, to contrast with the flower that surrounds it. Maybe make our practice name Harbor Bloom Care Clinic more feminine. Our practice caters to women only. All providers and staff are female.

Target Market(s)

Females 16-65.

Industry/Entity Type

Business

Contact Information for Business Card

See attached upload. The ONLY CHANGE to the information is DELETE the name Dorothy Kemplin, Midwife and REPLACE with Greta Poundsworth, Midwife

Logo Text

Harbor Bloom Care Clinic Obstetrics & Gynecology

Font styles to use
Serif
Script

Colors
85cae6
0692cd
33a6d7
85abd2
f59195
eea4c8
cadf82
fac994
d3a5cc

```html
<!DOCTYPE html>
<html lang="en">
<head>
<meta charset="utf-8">
<title>Harbor Bloom Care Clinic – Business Card</title>
<link href="https://fonts.googleapis.com/css2?family=Arimo:wght@400;700&family=Cinzel:wght@500&display=swap" rel="stylesheet">
<style>
  :root {
    --bg: #262626;
    --card-white: #f7f7f5;
    --card-grey: #6e6e6e;
    --teal: #7fbfd4;
    --teal-deep: #5fb0c9;
    --pink: #f2929a;
    --ink: #3f3f3f;
    --ink-soft: #555555;
    --stripe-grey: #6a6a6a;
  }
  * { box-sizing: border-box; margin: 0; padding: 0; }
  html, body { width: 1200px; height: 800px; overflow: hidden; }
  body {
    background: var(--bg);
    font-family: "Arimo", Arial, sans-serif;
    position: relative;
  }
  .card {
    position: absolute;
    width: 640px;
    height: 366px;
    overflow: hidden;
  }

  /* Back of card */
  .card-back {
    left: 440px;
    top: 24px;
    background: var(--card-grey);
  }
  .card-back .brand {
    position: absolute;
    left: 0; right: 0; top: 90px;
    display: flex; flex-direction: column; align-items: center; gap: 22px;
  }
  .brand-dot {
    width: 74px; height: 74px; border-radius: 50%;
    background: var(--teal);
    flex-shrink: 0;
  }
  .card-back .brand-name {
    font-family: "Cinzel", Georgia, serif;
    font-weight: 500;
    font-size: 26px;
    letter-spacing: 1px;
    color: #ffffff;
  }
  .card-back .web {
    position: absolute; left: 0; right: 0; bottom: 40px;
    text-align: center;
    font-size: 16px; letter-spacing: 3px; color: #ffffff;
  }
  .card-back .web .domain { color: var(--teal); font-weight: 700; }

  /* Front of card */
  .card-front {
    left: 120px;
    top: 410px;
    background: var(--card-white);
  }
  .front-brand {
    position: absolute; left: 34px; top: 30px;
    display: flex; align-items: center; gap: 16px;
  }
  .front-brand .brand-dot { width: 58px; height: 58px; }
  .front-brand .brand-name {
    font-family: "Cinzel", Georgia, serif;
    font-weight: 500; font-size: 21px; color: var(--teal-deep);
    letter-spacing: 0.5px;
  }
  .front-brand .tagline {
    font-size: 19px; font-weight: 700; color: var(--ink-soft); margin-top: 4px;
  }
  .address {
    position: absolute; left: 60px; top: 124px;
    font-size: 15px; line-height: 19px; color: var(--ink);
  }
  .divider {
    position: absolute; left: 60px; top: 172px;
    width: 380px; height: 2px; background: var(--teal);
  }
  .contact {
    position: absolute; left: 44px; top: 184px;
    list-style: none; font-size: 15px; line-height: 20px; color: var(--ink);
  }
  .contact li { display: flex; align-items: center; gap: 8px; }
  .contact svg { width: 13px; height: 13px; fill: none; stroke: var(--teal-deep); stroke-width: 1.6; }
  .providers {
    position: absolute; right: 34px; top: 160px;
    list-style: none; text-align: right;
    font-size: 16px; line-height: 20px; color: var(--ink);
  }
  .providers strong { font-weight: 700; }
  .waves { position: absolute; left: 0; top: 0; width: 640px; height: 366px; }
  .front-web {
    position: absolute; right: 34px; bottom: 20px;
    font-size: 18px; color: #ffffff; letter-spacing: 0.5px;
  }
  .front-web strong { font-weight: 700; }
</style>
</head>
<body>

<section class="card card-back" aria-label="Business card back">
  <div class="brand">
    <span class="brand-dot"></span>
    <span class="brand-name">Harbor Bloom Care Clinic</span>
  </div>
  <p class="web">www.<span class="domain">harborbloomcare</span>.com</p>
</section>

<section class="card card-front" aria-label="Business card front">
  <svg class="waves" viewBox="0 0 640 366" aria-hidden="true">
    <path d="M0,250 C100,280 220,312 320,322 L320,328 C200,320 100,296 0,272 Z" fill="var(--pink)"/>
    <path d="M420,304 C520,294 600,282 640,270 L640,288 C600,298 530,308 430,320 Z" fill="var(--stripe-grey)"/>
    <path d="M0,272 C140,310 300,336 430,320 C530,308 600,298 640,288 L640,366 L0,366 Z" fill="var(--teal)"/>
  </svg>

  <div class="front-brand">
    <span class="brand-dot"></span>
    <div>
      <p class="brand-name">Harbor Bloom Care Clinic</p>
      <p class="tagline">Obstetrics &amp; Gynecology</p>
    </div>
  </div>

  <p class="address">418 Larkspur Avenue<br>Suite 3B, Harbor City, GA 31099</p>
  <span class="divider"></span>

  <ul class="contact">
    <li><svg viewBox="0 0 14 14"><path d="M3 1 L5 4 L4 6 C5 8 6 9 8 10 L10 9 L13 11 L11 13 C6 12 2 8 1 3 Z"/></svg>(555) 014-2738</li>
    <li><svg viewBox="0 0 14 14"><rect x="2" y="5" width="10" height="6"/><rect x="4" y="1" width="6" height="4"/></svg>(555) 014-6153</li>
    <li><svg viewBox="0 0 14 14"><rect x="1" y="3" width="12" height="8"/><path d="M1 3 L7 8 L13 3"/></svg>info@harborbloomcare.com</li>
  </ul>

  <ul class="providers">
    <li><strong>Marian Ostrow,</strong> MD</li>
    <li><strong>Paula Brenton,</strong> MD</li>
    <li><strong>Nadine Folsom,</strong> MD</li>
    <li><strong>Greta Poundsworth,</strong> Midwife</li>
    <li><strong>Lena Hartwell,</strong> Midwife</li>
  </ul>

  <p class="front-web">www.<strong>harborbloomcare</strong>.com</p>
</section>

</body>
</html>
```